Bref créative
Stand out Biz Cards & Stationery for Quarvenix
A Cutting Edge Consulting & Executive Coaching Firm
Simple
Torben K. Aldavisto, PhD
President & CEO
48207 E Corvane Ave
Suite 2875-417
Phoenix, AZ 85093-6718
Torben@Aldavisto-mail.test
www.Aldavisto-mail.test
It might be questionable to use the tag line in the Logo since the font is very tiny.
The significant problems we have, cannot be solved at the same level of thinking with which we created them. -- Gustav Merriwold

```html
<!DOCTYPE html>
<html lang="en">
<head>
<meta charset="utf-8">
<title>Quarvenix Business Card</title>
<link rel="stylesheet" href="https://fonts.googleapis.com/css2?family=Source+Sans+3:wght@400;600&display=swap">
<style>
  :root {
    --backdrop: #e6e6e6;
    --card: #ffffff;
    --panel-top: #2b3a93;
    --panel-bottom: #1aa3e8;
    --ink: #555555;
    --brand-blue: #1f3f9a;
    --accent-red: #d7262e;
    --faint: #f6e2e2;
  }
  * { margin: 0; padding: 0; box-sizing: border-box; }
  html, body {
    width: 1200px; height: 901px; overflow: hidden;
    background: var(--backdrop);
    font-family: "Source Sans 3", sans-serif;
  }
  .card {
    position: absolute; top: 290px;
    width: 528px; height: 302px;
    background: var(--card);
    overflow: hidden;
  }
  .card--front { left: 34px; }
  .card--back { left: 638px; }

  .identity-panel {
    position: absolute; left: 0; top: 0; width: 263px; height: 100%;
    background: linear-gradient(180deg, var(--panel-top) 0%, var(--panel-bottom) 100%);
    color: #fff; text-align: center;
  }
  .identity-panel .name { margin-top: 22px; font-size: 16px; line-height: 1.3; }
  .identity-panel .title { font-size: 16px; line-height: 1.3; }
  .identity-panel .website {
    position: absolute; bottom: 16px; left: 0; right: 0; font-size: 15px;
  }

  .contact {
    position: absolute; left: 283px; top: 20px;
    font-size: 15px; line-height: 1.3; color: var(--ink);
    font-style: normal;
  }

  .brand {
    position: absolute; right: 22px; bottom: 30px;
    display: flex; align-items: center; gap: 8px;
  }
  .brand-mark { width: 18px; height: 18px; background: var(--accent-red); }
  .brand-name {
    font-size: 38px; font-weight: 600; color: var(--brand-blue);
    letter-spacing: 0.5px;
  }

  .back-decoration {
    position: absolute; left: 220px; top: 60px;
    width: 130px; height: 130px; border-radius: 50%;
    background: var(--faint);
  }
  .quote {
    position: absolute; left: 0; right: 0; top: 112px;
    text-align: center; font-size: 15px; line-height: 1.3; color: var(--ink);
  }
  .quote cite { display: block; font-style: normal; color: var(--accent-red); }
</style>
</head>
<body>
  <section class="card card--front">
    <div class="identity-panel">
      <p class="name">Torben K. Aldavisto, PhD</p>
      <p class="title">President &amp; CEO</p>
      <p class="website">www.Aldavisto-mail.test</p>
    </div>
    <address class="contact">
      48207 E Corvane Ave<br>
      Suite 2875-417<br>
      Phoenix, AZ 85093-6718<br>
      Phone: +1 (602) 555-0147<br>
      Email: Torben@Aldavisto-mail.test
    </address>
    <div class="brand">
      <span class="brand-mark"></span>
      <span class="brand-name">Quarvenix</span>
    </div>
  </section>

  <section class="card card--back">
    <div class="back-decoration"></div>
    <blockquote class="quote">
      The significant problems we have,<br>
      cannot be solved at the same level of thinking<br>
      with which we created them.
      <cite>-Gustav Merriwold-</cite>
    </blockquote>
  </section>
</body>
</html>
```